Capacity building in Resource Management

Need design of a business card (later to be completed by letterhead and webdesign in same fashion) for a professional who works in the field of capacity building of professionals in mostly developing countries in the field waste/resource management, waste prevention/reduction, cleaner production, stakeholders involvement, etc.
Info on business cards is to include provided logo, info in provided file and picture.

Industry/Entity Type

Business

Contact Information for Business Card

White background

Font styles to use
Sans Serif

Colors

Designer to choose colors to be used in the design.

```html
<!DOCTYPE html>
<html lang="en">
<head>
<meta charset="utf-8">
<title>Terra-Skola Business Card</title>
<link rel="stylesheet" href="https://fonts.googleapis.com/css2?family=Roboto+Condensed:wght@700&family=Roboto:wght@400&display=swap">
<style>
  :root {
    --bg: #d9dbdc;
    --card: #fbfbfa;
    --green: #4a8a2e;
    --green-dark: #3c7424;
    --grey: #6f6f6f;
    --text: #555555;
    --rule: #c9c9c9;
  }
  * { margin: 0; padding: 0; box-sizing: border-box; }
  html, body { width: 1200px; height: 900px; overflow: hidden; }
  body {
    background: var(--bg);
    font-family: "Roboto", Arial, sans-serif;
    position: relative;
  }
  .card {
    position: absolute;
    left: 300px;
    width: 600px;
    height: 350px;
    background: var(--card);
    box-shadow: 0 2px 8px rgba(0,0,0,0.15);
  }
  .card-front { top: 80px; }
  .card-back { top: 470px; }

  /* Front */
  .brand {
    position: absolute;
    top: 100px;
    left: 0;
    width: 100%;
    text-align: center;
  }
  .brand-name {
    display: inline-flex;
    align-items: center;
    gap: 12px;
    font-family: "Roboto Condensed", Arial, sans-serif;
    font-weight: 700;
    font-size: 46px;
    color: var(--green);
    line-height: 1;
  }
  .brand-dot {
    width: 22px; height: 22px;
    border-radius: 50%;
    background: var(--green);
  }
  .brand-tagline {
    margin-top: 8px;
    font-size: 13px;
    color: var(--grey);
    letter-spacing: 0.5px;
  }
  .front-web {
    position: absolute;
    top: 248px;
    width: 100%;
    text-align: center;
    font-size: 14px;
    letter-spacing: 7px;
    color: var(--text);
  }

  /* Back */
  .identity {
    position: absolute;
    right: 330px;
    top: 98px;
    text-align: right;
  }
  .identity-name {
    font-family: "Roboto Condensed", Arial, sans-serif;
    font-weight: 700;
    font-size: 34px;
    color: var(--green);
    line-height: 1;
  }
  .identity-tagline {
    margin-top: 6px;
    font-size: 16px;
    line-height: 1.15;
    color: var(--grey);
    text-transform: uppercase;
  }
  .divider {
    position: absolute;
    left: 287px;
    top: 92px;
    width: 1px;
    height: 132px;
    background: var(--rule);
  }
  .contacts {
    position: absolute;
    left: 305px;
    top: 96px;
    list-style: none;
  }
  .contact {
    display: flex;
    align-items: center;
    gap: 9px;
    font-size: 15px;
    line-height: 22px;
    color: var(--text);
  }
  .contact-icon {
    width: 13px; height: 13px;
    flex: none;
    fill: var(--green);
  }
  .address {
    position: absolute;
    left: 110px;
    top: 280px;
    display: flex;
    align-items: center;
    gap: 6px;
    font-size: 16px;
    color: var(--text);
  }
  .address .contact-icon { width: 14px; height: 16px; }
</style>
</head>
<body>
  <section class="card card-front">
    <div class="brand">
      <div class="brand-name"><span class="brand-dot"></span>terra-skola</div>
      <div class="brand-tagline">capacity building in resource management</div>
    </div>
    <div class="front-web">www.terra-skola.com</div>
  </section>

  <section class="card card-back">
    <div class="identity">
      <div class="identity-name">TERRA-SKOLA</div>
      <div class="identity-tagline">Capacity building in<br>resource management</div>
    </div>
    <div class="divider"></div>
    <ul class="contacts">
      <li class="contact">
        <svg class="contact-icon" viewBox="0 0 16 16"><path d="M3.5 1l2.5 3-1.5 2c1 2 3 4 5 5l2-1.5 3 2.5-1.5 2.5C8 16 0 8 1 2.5z"/></svg>
        +49 1520 347 8812 (also whatsapp)
      </li>
      <li class="contact">
        <svg class="contact-icon" viewBox="0 0 16 16"><path d="M1 3h14v10H1z M1 3l7 6 7-6" fill="none" stroke="#4a8a2e" stroke-width="1.6"/><path d="M1 3h14L8 9z"/></svg>
        lukas.brenner@terra-skola.com
      </li>
      <li class="contact">
        <svg class="contact-icon" viewBox="0 0 16 16"><circle cx="8" cy="8" r="6.5" fill="none" stroke="#4a8a2e" stroke-width="1.6"/><path d="M1.5 8h13M8 1.5c-3 3.5-3 9.5 0 13M8 1.5c3 3.5 3 9.5 0 13" fill="none" stroke="#4a8a2e" stroke-width="1.2"/></svg>
        www.terra-skola.com
      </li>
      <li class="contact">
        <svg class="contact-icon" viewBox="0 0 16 16"><circle cx="8" cy="8" r="6"/></svg>
        @lukasbrenner
      </li>
      <li class="contact">
        <svg class="contact-icon" viewBox="0 0 16 16"><circle cx="8" cy="8" r="6"/></svg>
        brenner2004
      </li>
      <li class="contact">
        <svg class="contact-icon" viewBox="0 0 16 16"><circle cx="8" cy="8" r="6"/></svg>
        Lukas Brenner
      </li>
    </ul>
    <div class="address">
      <svg class="contact-icon" viewBox="0 0 14 18"><path d="M7 0a6 6 0 0 0-6 6c0 4.5 6 12 6 12s6-7.5 6-12a6 6 0 0 0-6-6zm0 8.5A2.5 2.5 0 1 1 7 3.5a2.5 2.5 0 0 1 0 5z"/></svg>
      Lindenweg 12, 10117 Berlin, Germany
    </div>
  </section>
</body>
</html>
```